We are a church and would like a flyer for a special service that is held once a quarter to get families and friends to come out to join us. See below content and details for sizes.
Church Name: Covenant Harvest Global Fellowship
Church Logo : Attached
Title : Family and Friends Day
Subtitle: Strengthening Families - Connecting Relationships
Host: Bishop Kwame Dorlin (file attached. Don't need full body. Please crop)
Date: Sunday, 24 May
Time: 9:30 AM
Address: 2967 Marlow Lane, Suite F, Bowie MD, 20716
Phone : 240 913 2268
Website: www.chgfellowship.example
Flyer Size: Facebook size 851 x 314 pixels, Flash size 680 x 340 & Power Point size Standard

```html
<!DOCTYPE html>
<html lang="en">
<head>
<meta charset="utf-8">
<title>Family &amp; Friends Day – Covenant Harvest Global Fellowship</title>
<link rel="stylesheet" href="https://fonts.googleapis.com/css2?family=Aleo:wght@400;700&family=Berkshire+Swash&family=Cormorant+Garamond:wght@500&family=Roboto+Condensed:wght@400&display=swap">
<style>
  :root {
    --ink: #111111;
    --white: #ffffff;
    --sky: #4fb6d6;
    --sky-deep: #2f86c2;
    --cream: #f6eadb;
    --peach: #f3c7a4;
    --rose: #d9517e;
    --plum: #7a3a8a;
    --value-bg: rgba(222, 205, 188, 0.55);
    --ring: #8a7468;
    --header-ink: #1f2a36;
  }
  html, body {
    margin: 0;
    padding: 0;
    width: 1200px;
    height: 900px;
    overflow: hidden;
  }
  .flyer {
    position: relative;
    width: 1200px;
    height: 900px;
    overflow: hidden;
    font-family: "Aleo", Georgia, serif;
    color: var(--ink);
    background:
      radial-gradient(ellipse 620px 420px at 600px 430px, rgba(252,244,232,0.95) 0%, rgba(248,236,220,0.7) 45%, rgba(248,236,220,0) 100%),
      radial-gradient(ellipse 520px 380px at 1150px 60px, var(--sky-deep) 0%, rgba(47,134,194,0) 100%),
      radial-gradient(ellipse 520px 360px at 40px 760px, var(--plum) 0%, rgba(122,58,138,0) 100%),
      radial-gradient(ellipse 600px 320px at 280px 900px, var(--rose) 0%, rgba(217,81,126,0) 100%),
      radial-gradient(ellipse 520px 360px at 1180px 860px, var(--plum) 0%, rgba(122,58,138,0) 100%),
      linear-gradient(180deg, var(--sky) 0%, #9fd3df 22%, var(--cream) 48%, var(--peach) 72%, var(--rose) 100%);
  }
  .brand {
    position: absolute;
    left: 52px;
    top: 54px;
    display: flex;
    align-items: center;
    gap: 26px;
  }
  .brand-mark {
    width: 40px;
    height: 40px;
    border-radius: 50%;
    background: var(--sky-deep);
    margin-left: 18px;
  }
  .brand-name {
    font-family: "Roboto Condensed", Arial, sans-serif;
    font-size: 15px;
    letter-spacing: 2.2px;
    text-transform: uppercase;
    color: var(--header-ink);
  }
  .title {
    position: absolute;
    left: 0;
    width: 1200px;
    top: 188px;
    margin: 0;
    text-align: center;
    font-family: "Berkshire Swash", cursive;
    font-weight: 400;
    font-size: 86px;
    line-height: 100px;
    color: var(--ink);
  }
  .rule {
    position: absolute;
    left: 126px;
    width: 948px;
    height: 2px;
    background: var(--ink);
  }
  .rule-top { top: 301px; }
  .rule-bottom { top: 357px; }
  .subtitle {
    position: absolute;
    left: 0;
    width: 1200px;
    top: 311px;
    margin: 0;
    text-align: center;
    font-family: "Cormorant Garamond", Georgia, serif;
    font-weight: 500;
    font-size: 31px;
    line-height: 38px;
    color: #222;
    display: flex;
    justify-content: center;
    align-items: center;
    gap: 12px;
  }
  .subtitle svg { width: 22px; height: 22px; }
  .detail {
    position: absolute;
    height: 45px;
    display: flex;
    align-items: stretch;
    background: var(--white);
    box-sizing: border-box;
    padding: 3px 15px 3px 0;
  }
  .detail-label {
    width: 140px;
    flex: none;
    display: flex;
    align-items: center;
    padding-left: 18px;
    box-sizing: border-box;
    font-weight: 700;
    font-size: 22px;
  }
  .detail-value {
    flex: 1;
    display: flex;
    align-items: center;
    padding-left: 14px;
    background: linear-gradient(90deg, var(--value-bg), rgba(236,226,214,0.35));
    font-size: 22px;
    color: #1c1c1c;
  }
  .detail-date    { left: 122px; top: 421px; width: 463px; }
  .detail-time    { left: 614px; top: 421px; width: 463px; }
  .detail-phone   { left: 122px; top: 494px; width: 463px; }
  .detail-web     { left: 614px; top: 494px; width: 463px; }
  .detail-address { left: 122px; top: 566px; width: 955px; }
  .host-portrait {
    position: absolute;
    left: 876px;
    top: 641px;
    width: 154px;
    height: 154px;
    border-radius: 50%;
    box-sizing: border-box;
    border: 5px solid var(--ring);
    background: radial-gradient(circle at 50% 40%, #b9a79a 0%, #6d625c 55%, #3b3533 100%);
  }
  .host-role {
    position: absolute;
    left: 797px;
    top: 796px;
    font-size: 19px;
    color: rgba(255,255,255,0.75);
  }
  .host-name {
    position: absolute;
    left: 797px;
    top: 828px;
    font-size: 28px;
    color: var(--white);
  }
</style>
</head>
<body>
<main class="flyer">
  <header class="brand">
    <span class="brand-mark"></span>
    <span class="brand-name">Covenant Harvest Global Fellowship</span>
  </header>

  <h1 class="title">Family &amp; Friends Day</h1>
  <div class="rule rule-top"></div>
  <p class="subtitle">
    <span>Strengthening Families</span>
    <svg viewBox="0 0 24 24" aria-hidden="true"><path d="M12 1.5l3.1 7.1 7.6.6-5.8 5 1.8 7.5L12 17.7l-6.7 4 1.8-7.5-5.8-5 7.6-.6z" fill="#111"/></svg>
    <span>Connecting Relationships</span>
  </p>
  <div class="rule rule-bottom"></div>

  <div class="detail detail-date"><span class="detail-label">Date</span><span class="detail-value">24 May 2015 (Sunday)</span></div>
  <div class="detail detail-time"><span class="detail-label">Time</span><span class="detail-value">9:30 AM</span></div>
  <div class="detail detail-phone"><span class="detail-label">Phone</span><span class="detail-value">240 913 2268</span></div>
  <div class="detail detail-web"><span class="detail-label">Website</span><span class="detail-value">www.chgfellowship.example</span></div>
  <div class="detail detail-address"><span class="detail-label">Address</span><span class="detail-value">2967 Marlow Lane, Suite F, Bowie MD, 20716.</span></div>

  <div class="host-portrait" role="img" aria-label="Portrait photo of host Bishop Kwame Dorlin"></div>
  <div class="host-role">Host</div>
  <div class="host-name">Bishop Kwame Dorlin</div>
</main>
</body>
</html>
```